INNOVATIVE DESIGN NEEDED FOR FINANCIAL COMPANY

INTERNATIONAL FIRM IN HONG KONG NEEDS A MODERN BUSINESS CARD DESIGN. ONE SIDE ENGLISH OTHER SIDE IN CHINESE. WE ARE OPEN TO CHANGING FONTS AND COLOR. SHOULD BE A CARD THAT IS PROFESSIONAL DEALING WITH HIGH NET WORTH CLIENTELE. BOTH SIDES OF THE CARD WILL BE THE SAME, HOWEVER, THE WORDING ON ONE SIDE WILL BE ENGLISH AND THE OTHER SIDE IN CHINESE (CAN ASSIST IN THE LETTERING - CAN PROVIDE ONCE CARD DESIGN IS ACCEPTED.

Target Market(s)

Hong Kong/CHINA

Contact Information for Business Card

ATTRACTIVE MODERN

```html
<!DOCTYPE html>
<html lang="en">
<head>
<meta charset="utf-8">
<title>Aspen Crest Asset Management – Business Card</title>
<link rel="stylesheet" href="https://fonts.googleapis.com/css2?family=Archivo+Black&family=Noto+Sans+TC:wght@400;900&family=Noto+Serif+SC:wght@500&family=Roboto:wght@400;500&display=swap">
<style>
  :root {
    --bg: #2b2b2b;
    --card: #ffffff;
    --green: #16a37f;
    --green-deep: #138a4e;
    --ink: #3a3a3a;
    --text: #4a4a4a;
    --band-dark: #3d3d3d;
    --faint: #ecf5f1;
  }
  * { box-sizing: border-box; margin: 0; padding: 0; }
  html, body { width: 1200px; height: 1014px; overflow: hidden; background: var(--bg); }
  .sheet { position: relative; width: 1200px; height: 1014px; }
  .card {
    position: absolute; left: 170px; width: 860px; height: 491px;
    background: var(--card); overflow: hidden;
  }
  .card--front { top: 10px; }
  .card--back { top: 513px; }
  .faint-circle {
    position: absolute; right: 30px; top: 110px; width: 300px; height: 300px;
    border-radius: 50%; background: var(--faint);
  }
  .edge-bands { position: absolute; left: 0; bottom: 0; width: 860px; height: 70px; }
  .brand { position: absolute; left: 130px; top: 95px; display: flex; align-items: center; gap: 22px; }
  .brand__dot { width: 92px; height: 92px; border-radius: 50%; background: var(--green); flex: none; }
  .brand__name { font-family: "Noto Sans TC", sans-serif; font-weight: 900; color: var(--ink); }
  .brand__zh { font-size: 38px; letter-spacing: 3px; line-height: 1.1; }
  .brand__en { font-size: 17px; letter-spacing: 1.5px; line-height: 1.2; }
  .person { position: absolute; right: 110px; top: 215px; text-align: right; }
  .person__name--en { font-family: "Archivo Black", sans-serif; font-size: 34px; color: var(--green-deep); line-height: 1.1; }
  .person__name--zh { font-family: "Noto Serif SC", serif; font-weight: 500; font-size: 40px; color: var(--green-deep); letter-spacing: 3px; line-height: 1.1; }
  .person__role { font-family: "Roboto", sans-serif; font-size: 18px; color: var(--text); margin-top: 4px; }
  .person__role--zh { font-family: "Noto Sans TC", sans-serif; font-weight: 400; }
  .contacts { position: absolute; left: 60px; top: 300px; list-style: none; font-family: "Roboto", sans-serif; font-size: 19px; color: var(--text); }
  .contacts li { display: flex; align-items: flex-start; gap: 16px; margin-bottom: 9px; line-height: 26px; }
  .contacts .icon { width: 26px; height: 26px; flex: none; }
</style>
</head>
<body>
<div class="sheet">

  <!-- English side -->
  <section class="card card--front">
    <div class="faint-circle"></div>
    <div class="brand">
      <div class="brand__dot"></div>
      <div class="brand__name">
        <div class="brand__zh">安峰資產管理有限公司</div>
        <div class="brand__en">Aspen Crest Asset Management Ltd</div>
      </div>
    </div>
    <div class="person">
      <div class="person__name--en">Daniel Hartley</div>
      <div class="person__role">Managing Partner</div>
    </div>
    <ul class="contacts">
      <li><svg class="icon" viewBox="0 0 26 26"><circle cx="13" cy="13" r="13" fill="var(--green)"/><path d="M9 7.5l2.5 2.6-1.3 1.6a8 8 0 0 0 4.1 4.1l1.6-1.3 2.6 2.5-1.6 1.7c-4.5.2-9.6-4.9-9.4-9.4z" fill="#fff"/></svg><span>000 000 0000</span></li>
      <li><svg class="icon" viewBox="0 0 26 26"><circle cx="13" cy="13" r="13" fill="var(--green)"/><rect x="7" y="8.5" width="12" height="9" rx="1" fill="#fff"/><path d="M7.5 9.2l5.5 4.3 5.5-4.3" stroke="var(--green)" stroke-width="1.3" fill="none"/></svg><span>info@aspencrestam.com</span></li>
      <li><svg class="icon" viewBox="0 0 26 26"><circle cx="13" cy="13" r="13" fill="var(--green)"/><circle cx="13" cy="13" r="6.5" fill="none" stroke="#fff" stroke-width="1.5"/><ellipse cx="13" cy="13" rx="2.8" ry="6.5" fill="none" stroke="#fff" stroke-width="1.3"/><path d="M6.5 13h13" stroke="#fff" stroke-width="1.3"/></svg><span>www.aspencrestam.com</span></li>
      <li><svg class="icon" viewBox="0 0 26 26"><circle cx="13" cy="13" r="13" fill="var(--green)"/><path d="M7 13.5L13 8l6 5.5M9 12.5V18h8v-5.5" stroke="#fff" stroke-width="1.6" fill="none"/><rect x="11.8" y="14.5" width="2.4" height="3.5" fill="#fff"/></svg><span>2840 rue Beaulac<br>Ville Saint-Roch, QC J6K 2T4</span></li>
    </ul>
    <svg class="edge-bands" viewBox="0 0 860 70" preserveAspectRatio="none">
      <polygon points="330,70 860,70 860,52 345,56" fill="var(--green)"/>
      <polygon points="650,52 860,40 860,52" fill="var(--band-dark)"/>
    </svg>
  </section>

  <!-- Chinese side -->
  <section class="card card--back">
    <div class="faint-circle"></div>
    <div class="brand">
      <div class="brand__dot"></div>
      <div class="brand__name">
        <div class="brand__zh">安峰資產管理有限公司</div>
        <div class="brand__en">Aspen Crest Asset Management Ltd</div>
      </div>
    </div>
    <div class="person">
      <div class="person__name--zh">丹尼尔哈特利</div>
      <div class="person__role person__role--zh">管理伙伴</div>
    </div>
    <ul class="contacts">
      <li><svg class="icon" viewBox="0 0 26 26"><circle cx="13" cy="13" r="13" fill="var(--green)"/><path d="M9 7.5l2.5 2.6-1.3 1.6a8 8 0 0 0 4.1 4.1l1.6-1.3 2.6 2.5-1.6 1.7c-4.5.2-9.6-4.9-9.4-9.4z" fill="#fff"/></svg><span>000 000 0000</span></li>
      <li><svg class="icon" viewBox="0 0 26 26"><circle cx="13" cy="13" r="13" fill="var(--green)"/><rect x="7" y="8.5" width="12" height="9" rx="1" fill="#fff"/><path d="M7.5 9.2l5.5 4.3 5.5-4.3" stroke="var(--green)" stroke-width="1.3" fill="none"/></svg><span>info@aspencrestam.com</span></li>
      <li><svg class="icon" viewBox="0 0 26 26"><circle cx="13" cy="13" r="13" fill="var(--green)"/><circle cx="13" cy="13" r="6.5" fill="none" stroke="#fff" stroke-width="1.5"/><ellipse cx="13" cy="13" rx="2.8" ry="6.5" fill="none" stroke="#fff" stroke-width="1.3"/><path d="M6.5 13h13" stroke="#fff" stroke-width="1.3"/></svg><span>www.aspencrestam.com</span></li>
      <li><svg class="icon" viewBox="0 0 26 26"><circle cx="13" cy="13" r="13" fill="var(--green)"/><path d="M7 13.5L13 8l6 5.5M9 12.5V18h8v-5.5" stroke="#fff" stroke-width="1.6" fill="none"/><rect x="11.8" y="14.5" width="2.4" height="3.5" fill="#fff"/></svg><span>2840 rue Beaulac<br>Ville Saint-Roch, QC J6K 2T4</span></li>
    </ul>
    <svg class="edge-bands" viewBox="0 0 860 70" preserveAspectRatio="none">
      <polygon points="330,70 860,70 860,52 345,56" fill="var(--green)"/>
      <polygon points="650,52 860,40 860,52" fill="var(--band-dark)"/>
    </svg>
  </section>

</div>
</body>
</html>
```